Organic Infographic – "The 4 Pillars of Renewal"

Overview:
We are a coaching/education brand (Brightmoor Institute) and need a redesigned infographic illustrating our 4-area transformation model. Our current version (attached) uses a rigid, hard-edged triangle/pyramid layout — we want a completely new visual approach that feels organic, soft, and alive, since the topic is human personal development, not a technical process.

Content structure (please keep the wording, redesign the visual form):

4 areas: "Embodiment – The Foundation" and "Focus & Intuition Redefined – The Lens" sit on the same base level. "Heart Centered Living – The Bridge" sits one level above, connecting/enabling the other two. "Becoming Unlimited – The Peak" sits at the top, made possible by Heart Centered Living.
The 4 areas influence and inspire one another — this mutual connection must be visually recognizable (e.g. through overlapping zones, blended color transitions, connecting flowing lines, or similar). Areas may stay visually distinct; the connection between them is what must be shown.
Hierarchy should be expressed mainly through position/arrangement (ascending flow), not through size differences — all 4 areas should carry similar visual weight, since each is equally essential.
A supporting element: "The Brightmoor Methodology" with 3 phases (Phase 1: Awareness & Insight, Phase 2: Integration & Practice, Phase 3: Expansion & Sustainable Growth), each with a short description (text provided below).

Style direction:
Organic, soft, flowing shapes — no sharp angles or rigid geometric triangles. Attached are 3 moodboard references showing the direction we like: overlapping/blended circular shapes, flowing ribbon-style connections, and organic swirl divisions. Please don't copy any of them directly — combine this organic/overlapping visual language with our specific asymmetric hierarchy (2 areas base level + 1 bridge + 1 peak), which none of the references show exactly. This creative translation is the core task.

Icons: Please design one new, unified icon per area (4 total) plus 3 simple icons for the methodology phases — consistent style across all 7, your creative interpretation is welcome.

Typography: Headlines in Arsenal, body text in DM Sans.

Colors: Base palette — Embodiment D09176, Focus & Intuition Redefined B6623E, Heart Centered Living D9866B, Becoming Unlimited 6F7A70, dark text 23211A, light accent EACEC1. Slight adjustments are welcome if they improve visual distinction between areas.

Technical requirements (important):

Final files as vector format (SVG, AI, or EPS), with separated, editable, non-flattened/non-merged layers and paths.
Shapes should consist of simple, closed outline paths — no fine textures, no complex multi-stop gradients, no photorealistic rendering — since the artwork will later be manually redrawn as a whiteboard-animation video.
Primary format: 16:9 landscape. A secondary vertical/mobile version (3 outer areas stacked below the top area) is welcome but optional.

Usage rights: Full commercial usage across website, video, and social media required.

Attachments to include: current draft PDF (for text content and logo reference only — not for layout), our logo file, and the 3 moodboard reference images.

Budget: $100–150 — please let us know if this realistically allows for more designer participation, or advise on adjusting scope/budget

Methodology phase texts (for the 3 supporting icons):

Phase 1: Awareness & Insight
Cultivating self-reflection, identifying patterns, and gaining clarity on personal drivers through introspective practices and data-informed assessment.

Phase 2: Integration & Practice
Applying tools and frameworks, developing new habits, and aligning actions with core values through consistent application and feedback loops.

Phase 3: Expansion & Sustainable Growth
Achieving long-term transformation, exceeding limitations, and fostering resilience through continuous evolution and a purpose-driven approach.

```html
<!DOCTYPE html>
<html lang="en">
<head>
<meta charset="utf-8">
<title>Brightmoor Institute – The 4 Pillars of Renewal</title>
<link rel="stylesheet" href="https://fonts.googleapis.com/css2?family=Source+Serif+4:opsz,wght@8..60,600;8..60,700&family=DM+Sans:wght@400;500&display=swap">
<style>
  :root {
    --paper: #f4ebe2;
    --panel: #f1e7de;
    --ink: #23211a;
    --ink-soft: #3a362d;
    --sage: #6f7a70;
    --sage-light: #a7ae9f;
    --embody: #d09176;
    --focus: #c77a4c;
    --heart: #d9866b;
    --blush: #eacec1;
    --rose: #dba898;
    --copper: #b6623e;
    --line: #8a8a6a;
    --white: #fffaf5;
  }
  * { margin: 0; padding: 0; box-sizing: border-box; }
  html, body { width: 1200px; height: 675px; overflow: hidden; background: var(--paper); }
  .canvas { position: relative; width: 1200px; height: 675px; overflow: hidden; background: var(--paper); font-family: "DM Sans", sans-serif; color: var(--ink); }
  .art { position: absolute; inset: 0; }

  .brand { position: absolute; left: 30px; top: 26px; display: flex; align-items: center; gap: 12px; }
  .brand-dot { width: 14px; height: 14px; border-radius: 50%; background: var(--rose); }
  .brand-name { font-family: "Source Serif 4", serif; font-weight: 700; font-size: 30px; color: var(--ink); }
  .tagline { position: absolute; left: 30px; top: 105px; font-size: 7.5px; letter-spacing: 2.6px; color: var(--ink-soft); }

  .intro { position: absolute; left: 26px; top: 146px; width: 170px; }
  .intro-rule { width: 1px; height: 28px; background: var(--copper); margin-left: 2px; margin-bottom: 36px; }
  .intro-title { font-family: "Source Serif 4", serif; font-weight: 700; font-size: 25px; line-height: 27px; }
  .intro-text { margin-top: 14px; font-size: 14px; line-height: 19.5px; color: var(--ink-soft); }
  .intro-end { width: 28px; height: 1px; background: var(--copper); margin-top: 22px; }

  .callout { position: absolute; font-size: 11.3px; line-height: 14.6px; color: var(--ink-soft); }
  .callout.center { text-align: center; }

  .panel { position: absolute; left: 760px; top: 24px; width: 417px; height: 562px; border-radius: 44px; background: var(--panel); border: 1px solid #e6d9cc; }
  .panel-icons { position: absolute; left: 0; top: 0; width: 160px; height: 520px; }
  .panel-title { position: absolute; left: 45px; top: 24px; font-family: "Source Serif 4", serif; font-weight: 700; font-size: 34px; line-height: 36px; }
  .panel-sub { position: absolute; left: 45px; top: 104px; font-size: 9px; letter-spacing: 3.6px; color: var(--ink-soft); }
  .phase { position: absolute; left: 132px; width: 280px; }
  .phase-num { position: absolute; left: 0; top: -3px; width: 31px; height: 31px; border-radius: 50%; color: var(--white); font-family: "Source Serif 4", serif; font-weight: 700; font-size: 16px; display: flex; align-items: center; justify-content: center; }
  .phase-title { margin-left: 43px; font-family: "Source Serif 4", serif; font-weight: 700; font-size: 16.5px; letter-spacing: -0.5px; line-height: 22px; white-space: nowrap; }
  .phase-text { margin-left: 43px; margin-top: 6px; width: 232px; font-size: 11.4px; line-height: 15.2px; color: var(--ink-soft); }
  .panel-foot { position: absolute; left: 0; right: 0; top: 531px; text-align: center; font-size: 9px; letter-spacing: 3.4px; color: var(--ink-soft); }
  .panel-foot::before { content: ""; position: absolute; left: 64px; right: 64px; top: -14px; height: 1px; background: #cbbdaf; }

  .motto { position: absolute; right: 48px; top: 623px; text-align: right; font-size: 9.5px; line-height: 15px; letter-spacing: 3.2px; color: var(--white); }
</style>
</head>
<body>
<div class="canvas">
  <svg class="art" viewBox="0 0 1200 675" aria-hidden="true">
    <path d="M0,560 C150,520 300,600 470,590 C640,580 700,560 800,600 C900,640 1000,570 1200,585 L1200,675 L0,675Z" fill="#ead8ca"/>
    <path d="M0,590 C120,565 230,620 380,630 C520,640 560,610 700,640 L700,675 L0,675Z" fill="#dcc2b0" opacity=".7"/>
    <path d="M560,660 C720,630 860,640 980,610 C1060,590 1120,590 1200,600 L1200,675 L560,675Z" fill="var(--sage-light)"/>
    <path d="M820,675 C920,640 1030,630 1200,625 L1200,675Z" fill="var(--sage)" opacity=".8"/>

    <path d="M330,240 C320,150 350,40 455,32 C560,28 600,130 590,230 C660,300 760,360 740,470 C720,570 600,590 520,560 C470,545 430,545 390,565 C300,600 150,570 145,470 C140,370 250,320 330,240Z" fill="#ebdccf" opacity=".7"/>

    <path d="M338,160 C330,80 390,30 460,32 C535,34 585,95 575,170 C570,230 525,260 455,258 C385,256 344,220 338,160Z" fill="var(--sage-light)" opacity=".55"/>
    <path d="M358,155 C352,85 405,42 462,44 C525,46 565,100 558,162 C552,212 510,232 455,230 C398,228 362,200 358,155Z" fill="var(--sage)" opacity=".9"/>

    <path d="M320,330 C320,270 380,242 455,242 C530,242 585,272 582,330 C580,395 520,455 455,458 C390,455 322,395 320,330Z" fill="var(--blush)" opacity=".85"/>
    <path d="M362,330 C362,280 405,258 455,258 C510,258 552,282 550,332 C548,385 505,425 455,428 C405,425 362,385 362,330Z" fill="var(--heart)" opacity=".9"/>

    <path d="M150,470 C150,400 210,372 280,375 C350,378 395,420 392,480 C390,540 335,565 270,562 C200,560 150,530 150,470Z" fill="var(--rose)" opacity=".6"/>
    <path d="M178,470 C178,418 225,392 280,394 C338,396 375,428 372,478 C370,528 325,548 272,546 C215,544 178,518 178,470Z" fill="var(--embody)" opacity=".9"/>

    <path d="M490,480 C490,410 545,372 620,375 C700,378 738,430 735,490 C732,550 680,578 612,575 C540,572 490,545 490,480Z" fill="#e2a47e" opacity=".65"/>
    <path d="M515,485 C515,425 560,395 620,397 C685,399 715,440 712,492 C710,542 668,566 612,564 C555,562 515,538 515,485Z" fill="var(--focus)" opacity=".92"/>

    <g fill="none" stroke="var(--line)" stroke-width="1">
      <path d="M305,575 C360,560 380,500 395,440 C415,350 300,360 260,280 C235,230 330,240 365,230"/>
      <path d="M420,600 C300,630 160,600 190,570"/>
      <path d="M520,240 C580,200 600,130 560,90"/>
      <path d="M560,460 C600,380 520,320 530,240"/>
      <path d="M420,430 C400,300 360,260 365,230"/>
    </g>
    <g fill="none" stroke="var(--line)" stroke-width="1.1" stroke-dasharray="3 3">
      <path d="M265,265 C280,240 300,220 328,212"/>
      <path d="M582,206 C620,220 640,250 638,280"/>
    </g>
    <g fill="none" stroke="var(--line)" stroke-width="1.2" stroke-linecap="round">
      <path d="M322,207 L328,212 L320,216"/>
      <path d="M365,238 L365,228 M360,233 L365,228 L370,233"/>
      <path d="M530,245 L530,235 M525,240 L530,235 L535,240"/>
      <path d="M410,502 C440,490 460,490 483,502"/>
      <path d="M416,497 L410,502 L417,506 M477,497 L483,502 L476,506"/>
      <path d="M533,72 L582,72"/>
      <path d="M592,305 L618,305"/>
    </g>
    <circle cx="533" cy="72" r="3.5" fill="var(--ink-soft)"/>
    <circle cx="594" cy="305" r="3" fill="var(--ink-soft)"/>
    <circle cx="581" cy="206" r="2.5" fill="var(--ink-soft)"/>

    <g fill="none" stroke="var(--white)" stroke-width="1.8" stroke-linecap="round" stroke-linejoin="round">
      <path d="M422,132 L446,108 L454,116 L462,108 L486,132"/>
      <path d="M454,108 L454,82 M454,92 C444,88 440,80 442,72 C450,74 455,82 454,92 M454,86 C462,80 468,74 466,66 C458,68 452,76 454,86"/>
      <path d="M453,314 C438,302 430,294 430,284 C430,276 437,272 443,272 C448,272 451,275 453,279 C455,275 458,272 463,272 C469,272 476,276 476,284 C476,294 468,302 453,314Z"/>
      <path d="M453,260 L453,266 M425,270 L430,274 M481,270 L476,274 M418,292 L424,292 M488,292 L482,292"/>
      <circle cx="265" cy="426" r="7"/>
      <path d="M265,440 L265,478 M265,455 C250,445 240,448 238,460 C250,468 260,466 265,455 M265,455 C280,445 290,448 292,460 C280,468 270,466 265,455"/>
      <path d="M595,452 C605,438 617,432 623,432 C629,432 641,438 651,452 C641,466 629,472 623,472 C617,472 605,466 595,452Z"/>
      <circle cx="623" cy="452" r="8"/>
      <path d="M623,420 L623,428 M605,424 L609,431 M641,424 L637,431"/>
    </g>

    <g font-family="'Source Serif 4', serif" font-weight="700" fill="var(--white)" text-anchor="middle" font-size="22">
      <text x="454" y="161">Becoming</text>
      <text x="454" y="184">Unlimited</text>
      <text x="454" y="347">Heart Centered</text>
      <text x="454" y="371">Living</text>
      <text x="265" y="508">Embodiment</text>
      <text x="628" y="501">Focus &amp; Intuition</text>
      <text x="628" y="524">Redefined</text>
    </g>
    <g font-family="'DM Sans', sans-serif" fill="var(--white)" text-anchor="middle" font-size="10" letter-spacing="4">
      <text x="454" y="205">THE PEAK</text>
      <text x="454" y="392">THE BRIDGE</text>
      <text x="265" y="532">THE FOUNDATION</text>
      <text x="628" y="546">THE LENS</text>
    </g>
  </svg>

  <div class="brand"><span class="brand-dot"></span><span class="brand-name">Brightmoor Institute</span></div>
  <div class="tagline">LEGENDS &nbsp;•&nbsp; PURPOSE &nbsp;•&nbsp; A BRIGHTER TOMORROW</div>

  <section class="intro">
    <div class="intro-rule"></div>
    <h1 class="intro-title">Four<br>Areas.<br>A Fuller You.</h1>
    <p class="intro-text">Different paths.<br>A shared purpose.<br>A more alive, authentic, and unlimited you.</p>
    <div class="intro-end"></div>
  </section>

  <p class="callout" style="left:592px;top:54px;width:130px;">Continuously rise, expand, and redefine your potential.</p>
  <p class="callout" style="left:625px;top:288px;width:100px;">Connect and align, enabling transformation of body and mind.</p>
  <p class="callout center" style="left:386px;top:527px;width:140px;">All areas influence and inspire one another.</p>
  <p class="callout center" style="left:180px;top:579px;width:180px;">Ground the journey with presence, vitality, and self-trust.</p>
  <p class="callout center" style="left:540px;top:580px;width:170px;">Bring clarity, inner guidance, and conscious direction.</p>

  <section class="panel">
    <svg class="panel-icons" viewBox="0 0 160 520" aria-hidden="true">
      <circle cx="74" cy="182" r="47" fill="var(--rose)" opacity=".85"/>
      <circle cx="74" cy="313" r="49" fill="var(--copper)" opacity=".9"/>
      <circle cx="74" cy="449" r="49" fill="var(--sage)" opacity=".9"/>
      <g stroke="var(--copper)" stroke-width="1">
        <line x1="74" y1="236" x2="74" y2="258"/>
        <line x1="74" y1="370" x2="74" y2="392"/>
      </g>
      <g fill="none" stroke="var(--white)" stroke-width="1.8" stroke-linecap="round" stroke-linejoin="round">
        <path d="M74,204 L74,174 M74,184 C64,180 60,172 62,164 C70,166 75,174 74,184 M74,178 C82,172 87,166 85,158 C77,160 72,168 74,178"/>
        <circle cx="60" cy="326" r="12"/><circle cx="60" cy="326" r="5"/>
        <circle cx="88" cy="302" r="10"/><circle cx="88" cy="302" r="4"/>
        <path d="M60,310 L60,314 M60,338 L60,342 M44,326 L48,326 M72,326 L76,326 M88,288 L88,292 M88,312 L88,316 M74,302 L78,302 M98,302 L102,302"/>
        <path d="M74,478 L74,432 M74,478 C66,462 66,444 74,432 C82,444 82,462 74,478 M74,478 C60,474 48,464 46,452 C60,452 70,464 74,478 M74,478 C88,474 100,464 102,452 C88,452 78,464 74,478"/>
      </g>
    </svg>
    <h2 class="panel-title">The Brightmoor<br>Methodology</h2>
    <p class="panel-sub">A 3-PHASE PATH TO LASTING TRANSFORMATION</p>
    <div class="phase" style="top:146px;">
      <span class="phase-num" style="background:var(--rose)">1</span>
      <h3 class="phase-title">Awareness &amp; Insight</h3>
      <p class="phase-text">Cultivating self-reflection, identifying patterns, and gaining clarity on personal drivers through introspective practices and data-informed assessment.</p>
    </div>
    <div class="phase" style="top:274px;">
      <span class="phase-num" style="background:var(--copper)">2</span>
      <h3 class="phase-title">Integration &amp; Practice</h3>
      <p class="phase-text">Applying tools and frameworks, developing new habits, and aligning actions with core values through consistent application and feedback loops.</p>
    </div>
    <div class="phase" style="top:407px;">
      <span class="phase-num" style="background:var(--sage)">3</span>
      <h3 class="phase-title">Expansion &amp; Sustainable Growth</h3>
      <p class="phase-text">Achieving long-term transformation, exceeding limitations, and fostering resilience through continuous evolution and a purpose-driven approach.</p>
    </div>
    <p class="panel-foot">REAL PEOPLE. LASTING CHANGE.</p>
  </section>

  <p class="motto">A MORE HUMAN WAY<br>TO GROW &nbsp;——</p>
</div>
</body>
</html>
```